Tidewell Outfitters Mobile RV Repair

We are looking for a logo and business cards for a new start up business. We will be doing Mobile RV Repair.
We are in Texas.
I don't have any designs at this point.

Contact Information for Business Card

Emphasis should be on the “Mobile RV Repair” and not so much the name “Tidewell Outfitters”

Requirements
Nice to have
• I like the Mobile RV Repair to cover most of the backside of the card! Not sure on the colors, would like to see it in a few different colors!

```html
<!DOCTYPE html>
<html lang="en">
<head>
<meta charset="utf-8">
<title>Tidewell Outfitters Mobile RV Repair – Business Cards</title>
<link rel="stylesheet" href="https://fonts.googleapis.com/css2?family=Montserrat:wght@600;700&family=Poppins:wght@400;600;700&display=swap">
<style>
  :root {
    --page-bg: #d9d4cc;
    --card-black: #1b1b1c;
    --card-dark: #262628;
    --silver-light: #f4f4f4;
    --silver-mid: #bdbdbd;
    --silver-dark: #7d7d7d;
    --orange: #f7861e;
    --white: #ffffff;
    --name-grey: #c9c9c9;
  }
  * { margin: 0; padding: 0; box-sizing: border-box; }
  html, body { width: 900px; height: 1200px; overflow: hidden; }
  body { background: var(--page-bg); position: relative; font-family: "Poppins", sans-serif; }

  .card {
    position: absolute;
    left: 82px;
    width: 733px;
    height: 430px;
    border-radius: 20px;
    overflow: hidden;
    background: var(--card-black);
  }
  .card--front { top: 138px; }
  .card--back { top: 633px; }
  .card-art { position: absolute; inset: 0; width: 733px; height: 430px; }

  .holder-name {
    position: absolute; left: 32px; top: 70px;
    font-family: "Montserrat", sans-serif; font-weight: 700;
    font-size: 23px; letter-spacing: 2px; color: var(--name-grey);
  }

  .brand-mark {
    position: absolute;
    font-family: "Poppins", sans-serif; font-weight: 700;
    color: var(--white); text-transform: uppercase; text-align: center;
    line-height: 1.1;
  }
  .brand-mark .brand-name { display: block; }
  .brand-mark .brand-service { display: block; }
  .card--front .brand-mark { left: 440px; top: 130px; width: 270px; }
  .card--front .brand-name { font-size: 22px; }
  .card--front .brand-service { font-size: 25px; margin-top: 4px; }
  .card--back .brand-mark { left: 166px; top: 140px; width: 400px; }
  .card--back .brand-name { font-size: 30px; }
  .card--back .brand-service { font-size: 40px; margin-top: 6px; }

  .contact-list { position: absolute; left: 32px; top: 326px; list-style: none; }
  .contact-item {
    display: flex; align-items: center; gap: 10px;
    color: var(--white); margin-bottom: 8px;
  }
  .contact-item--phone { font-size: 20px; font-weight: 600; }
  .contact-item--email { font-size: 17px; font-weight: 400; }
  .contact-icon { width: 18px; height: 18px; flex: none; }
</style>
</head>
<body>

  <section class="card card--front" aria-label="Business card front">
    <svg class="card-art" viewBox="0 0 733 430" aria-hidden="false">
      <defs>
        <linearGradient id="silverSweep" x1="0" y1="0" x2="1" y2="0">
          <stop offset="0" stop-color="var(--silver-dark)"/>
          <stop offset="0.35" stop-color="var(--silver-light)"/>
          <stop offset="0.7" stop-color="var(--silver-mid)"/>
          <stop offset="1" stop-color="var(--silver-light)"/>
        </linearGradient>
        <linearGradient id="meshTone" x1="0" y1="0" x2="1" y2="1">
          <stop offset="0" stop-color="#3a3a3c"/>
          <stop offset="0.6" stop-color="#5a5a5c"/>
          <stop offset="1" stop-color="#2b2b2d"/>
        </linearGradient>
        <linearGradient id="darkPanel" x1="0" y1="0" x2="0" y2="1">
          <stop offset="0" stop-color="var(--card-dark)"/>
          <stop offset="1" stop-color="var(--card-black)"/>
        </linearGradient>
      </defs>
      <rect width="733" height="430" fill="url(#darkPanel)"/>
      <path role="img" aria-label="Metallic honeycomb mesh texture" fill="url(#meshTone)"
            d="M150,0 C320,30 440,170 733,255 L733,355 C650,370 560,350 450,280 C330,200 200,150 0,160 L0,0 Z"
            opacity="0.55"/>
      <path fill="var(--card-black)" d="M0,0 L150,0 C280,25 360,90 330,110 C240,150 120,150 0,150 Z" opacity="0.85"/>
      <path fill="none" stroke="url(#silverSweep)" stroke-width="6" d="M150,0 C320,30 440,170 733,255"/>
      <path fill="url(#silverSweep)"
            d="M0,158 C200,146 330,198 450,278 C560,350 650,368 733,352 L733,376 C640,396 550,382 438,310 C320,232 200,186 0,186 Z"/>
      <path fill="none" stroke="var(--silver-mid)" stroke-width="2" d="M0,200 C220,205 330,260 460,330 C570,390 660,400 733,392"/>
    </svg>

    <p class="holder-name">DANA WHITLOW</p>

    <div class="brand-mark">
      <span class="brand-name">Tidewell Outfitters</span>
      <span class="brand-service">Mobile RV Repair</span>
    </div>

    <ul class="contact-list">
      <li class="contact-item contact-item--phone">
        <svg class="contact-icon" viewBox="0 0 24 24"><path fill="var(--orange)" d="M6.6 10.8a15.2 15.2 0 0 0 6.6 6.6l2.2-2.2a1 1 0 0 1 1-.25 11.4 11.4 0 0 0 3.6.57 1 1 0 0 1 1 1V20a1 1 0 0 1-1 1A17 17 0 0 1 3 4a1 1 0 0 1 1-1h3.5a1 1 0 0 1 1 1c0 1.25.2 2.45.57 3.57a1 1 0 0 1-.25 1Z"/></svg>
        512-555-0148
      </li>
      <li class="contact-item contact-item--email">
        <svg class="contact-icon" viewBox="0 0 24 24"><rect x="2" y="5" width="20" height="14" rx="1" fill="var(--orange)"/><path d="M2.5 5.5 12 13l9.5-7.5" fill="none" stroke="var(--card-black)" stroke-width="1.6"/></svg>
        TidewellRV@mailbox.com
      </li>
    </ul>
  </section>

  <section class="card card--back" aria-label="Business card back">
    <svg class="card-art" viewBox="0 0 733 430">
      <defs>
        <linearGradient id="silverBand" x1="0" y1="0" x2="1" y2="0">
          <stop offset="0" stop-color="var(--silver-mid)"/>
          <stop offset="0.4" stop-color="var(--silver-light)"/>
          <stop offset="0.75" stop-color="var(--silver-dark)"/>
          <stop offset="1" stop-color="var(--silver-light)"/>
        </linearGradient>
        <radialGradient id="backPanel" cx="0.5" cy="0.5" r="0.7">
          <stop offset="0" stop-color="#2c2c2e"/>
          <stop offset="1" stop-color="var(--card-black)"/>
        </radialGradient>
      </defs>
      <rect width="733" height="430" fill="url(#backPanel)"/>
      <path fill="url(#silverBand)" d="M0,0 L733,0 L733,98 C600,60 420,30 260,28 C150,28 60,50 0,75 Z"/>
      <path fill="var(--card-black)" d="M0,0 L733,0 L733,40 C560,10 380,0 200,10 C110,15 40,25 0,38 Z" opacity="0.25"/>
      <path fill="none" stroke="var(--silver-light)" stroke-width="2" d="M0,82 C80,55 170,36 270,36 C430,38 600,70 733,106"/>
      <path fill="url(#silverBand)"
            d="M0,300 C120,292 240,340 400,348 C540,354 650,330 733,300 L733,330 C650,355 540,378 400,372 C240,366 120,330 0,336 Z"/>
      <path fill="var(--orange)"
            d="M0,350 C140,340 260,385 420,388 C560,390 660,360 733,335 L733,430 L0,430 Z"/>
    </svg>

    <div class="brand-mark">
      <span class="brand-name">Tidewell Outfitters</span>
      <span class="brand-service">Mobile RV Repair</span>
    </div>
  </section>

</body>
</html>
```